Gallant Paddock Banner

Hi, I need a banner design for a roll up banner 85cm x 200cm.. our colours are dark green gray and white it would be great if you can let that come back… I will attach an example of how I would like it.. I would like to add the picture my self so I can change it every year. Also add our socials from Facebook and instagram as also our website:
Fb: ORK Bramstede/ PV Het Laarveld
Instagram: ORKBRAMSTEDE
Website: www.pvhetlaarveld.nl

The place where it will be held is: Velderam

Target Market(s)

Het people to the event.

Industry/Entity Type

Equestrian

Font styles to use
Serif
Sans Serif
Decorative

Colors
00AB8E
00BBA5
67D7C9
C6EFE9
E9F9F6

Requirements
Must have
• See description
Nice to have
• I added an idea for you to copy
Should not have
• The text: GRATIS ENTREE

```html
<!DOCTYPE html>
<html lang="nl">
<head>
<meta charset="utf-8">
<title>PV Het Laarveld – Roll-up banner</title>
<link rel="stylesheet" href="https://fonts.googleapis.com/css2?family=Anton&family=Bodoni+Moda:wght@400&family=Poppins:wght@500;600;700&display=swap">
<style>
  :root{
    --green:#0c6d4d;
    --ink:#1d1d1d;
    --white:#ffffff;
    --sky-top:#b7dad9;
    --sky-mid:#e3f0ef;
    --flag-blue:#2d4a8a;
    --flag-red:#d63a5a;
  }
  *{margin:0;padding:0;box-sizing:border-box}
  html,body{width:1200px;height:2400px;overflow:hidden;background:#dcdcdc}
  .banner{position:relative;width:1200px;height:2400px;overflow:hidden;
    background:linear-gradient(180deg,var(--sky-top) 0%,var(--sky-mid) 14%,#f6f8f8 26%,#ffffff 40%);}
  .artwork{position:absolute;inset:0;width:1200px;height:2400px}
  .brand{position:absolute;top:108px;left:0;width:1200px;text-align:center}
  .brand-mark{width:250px;height:250px;border-radius:50%;border:6px solid var(--green);margin:0 auto;transform:translateX(34px)}
  .brand-name{margin-top:14px;font-family:"Bodoni Moda",serif;font-weight:400;font-size:82px;line-height:1.1;color:var(--green);letter-spacing:1px;transform:translateX(34px)}
  .event-title{position:absolute;top:1541px;left:0;width:1200px;text-align:center;
    font-family:"Anton",sans-serif;font-weight:400;font-size:487px;line-height:1;color:var(--ink);letter-spacing:6px}
  .location{position:absolute;top:2004px;left:182px;width:838px;height:100px;background:var(--green);
    display:flex;align-items:center;justify-content:center;gap:26px;
    font-family:"Poppins",sans-serif;font-weight:600;font-size:86px;color:var(--white);line-height:1}
  .location svg{width:46px;height:64px}
  .location span{position:relative;top:4px}
  .socials{position:absolute;top:2114px;left:150px;list-style:none;font-family:"Poppins",sans-serif;font-weight:500;font-size:46px;color:var(--ink)}
  .social{display:flex;align-items:center;gap:34px;height:66px}
  .social-dot{width:44px;height:44px;border-radius:8px;background:var(--green)}
  .website{position:absolute;top:2250px;left:0;width:1200px;text-align:center;line-height:1.2;
    font-family:"Poppins",sans-serif;font-weight:700;font-size:58px;letter-spacing:10px;color:var(--ink)}
  .website .domain{color:var(--green)}
</style>
</head>
<body>
<main class="banner">
  <svg class="artwork" viewBox="0 0 1200 2400" xmlns="http://www.w3.org/2000/svg">
    <defs>
      <linearGradient id="photoTone" x1="0" y1="0" x2="1" y2="1">
        <stop offset="0" stop-color="#e9ecef"/>
        <stop offset="0.45" stop-color="#6b3a22"/>
        <stop offset="1" stop-color="#3c2012"/>
      </linearGradient>
      <linearGradient id="arenaTone" x1="0" y1="0" x2="0" y2="1">
        <stop offset="0" stop-color="#ececec"/>
        <stop offset="1" stop-color="#dedede"/>
      </linearGradient>
    </defs>
    <polygon class="flag-blue" points="0,563 0,651 560,880 600,790" fill="var(--flag-blue)"/>
    <polygon class="flag-red" points="0,792 0,889 620,1170 640,1060" fill="var(--flag-red)"/>
    <path class="arena-photo" role="img" aria-label="Faded photo of the show arena and grandstand"
      d="M0,1082 C150,1140 250,1250 420,1340 C620,1450 900,1480 1200,1654 L1200,2400 L0,2400 Z" fill="url(#arenaTone)"/>
    <path class="feature-photo" role="img" aria-label="Event photo: show jumper and rider clearing a fence (replaceable each year)"
      d="M300,760 C420,620 560,520 720,475 L1200,475 L1200,1654 C1100,1600 1000,1560 900,1530 C700,1470 480,1420 420,1340 C360,1180 300,980 300,760 Z" fill="url(#photoTone)"/>
    <path class="green-sweep" d="M0,1082 C150,1140 250,1250 420,1340 C620,1450 900,1480 1200,1654"
      fill="none" stroke="var(--green)" stroke-width="24" stroke-linecap="round"/>
  </svg>

  <header class="brand">
    <div class="brand-mark"></div>
    <div class="brand-name">PV Het Laarveld</div>
  </header>

  <h1 class="event-title">CSIO</h1>

  <div class="location">
    <svg viewBox="0 0 24 34" aria-hidden="true"><path d="M12 0C5.4 0 0 5.2 0 11.7 0 20 12 34 12 34s12-14 12-22.3C24 5.2 18.6 0 12 0zm0 16.5a5 5 0 1 1 0-10 5 5 0 0 1 0 10z" fill="#fff"/></svg>
    <span>VELDERAM</span>
  </div>

  <ul class="socials">
    <li class="social"><span class="social-dot"></span><span>ORK Bramstede/ PV Het Laarveld</span></li>
    <li class="social"><span class="social-dot"></span><span>ORKBRAMSTEDE</span></li>
  </ul>

  <p class="website">www.<span class="domain">pvhetlaarveld</span>.nl</p>
</main>
</body>
</html>
```